I require a very professional looking stationary set to include: letterhead, compliments slip and business cards (double sided bus cards).

Please design the following:-

•Create a Stationery Design
•Business Card Required.
•Letterhead Required.
•Compliments slip required
•Logo to use within email signature

I am an accountant that requires a corporate identity creating. I would like a professional yet simple theme that can be printed on letterheads and inserted into email signatures.

My website is www.tbhenley.co.uk

I am not a typical accountant as I offer part-time finance director services (CFO) to growing, small & medium sized companies (not individuals) and my main communication method is via business card and email (I do not issue brochures) therefore I want a high quality professional design.

Information I would like on the letterhead, compliment slip & business cards:-

Tom Henley (FCMA)

Thomas Henley Limited
Willow Brook Cottage
Fenn
Ashcombe
Merrowshire
TR8 2PW

tbhenley@tbhenley.co.uk
www.tbhenley.co.uk

Mobile number: 07700-900412

With a tag line: - Full time results / Part time costs

The tag line needs to be editable in the future.

The business card needs to be double sided and list the following services that I offer (to be editable if required):-

-Management accounting
-Interim management
-Business plans
-Budgeting & forecasting
-Payroll services
-Project management

In summary the overall image that I would like to project is :-

Professional, proactive, team player, adding value, trusted.
Updates

I would like a new logo that is different to my existing logo - my website is for info. about what I do.

I will be redesigning my website after deciding on a new Corporate Identity.

Please ask if further clarification is required.

Thanks
Tom

Please include

"Providing Part time Finance Director Services"

above the tag line

"Full time results / Part time costs"

Thanks
Tom 

Update for the letterhead - no footer is required
Thanks
Tom

Hi,

Please note that I would like a NEW logo designed to on on the stationery.

Please ask if you have any queries.

Thanks
Tom

Target Market(s)

Small & medium sized businesses who require a Finance Director or CFO but cannot afford one fulll time.

Industry/Entity Type

Communication

Requirements
Must have
• Concurrent theme with business cards, letterhead and comp slip & logo. Must be an editable document for future amendment (eg Word doc)
Nice to have
• Modern design, sans fonts, simple design
Should not have
• Watermark or be more than 2 colours. Photographs, images of people, money, calculators or currency symbols.

```html
<!DOCTYPE html>
<html lang="en">
<head>
<meta charset="utf-8">
<title>Thomas Henley Limited – Stationery</title>
<link href="https://fonts.googleapis.com/css2?family=Questrial&display=swap" rel="stylesheet">
<style>
  :root{
    --slate:#5a6781;
    --ink:#3d3d3d;
    --paper:#ffffff;
    --backdrop:#e4e4e4;
    --rule:#8a93a6;
  }
  *{box-sizing:border-box;margin:0;padding:0}
  html,body{width:1200px;height:900px;overflow:hidden}
  body{
    background:var(--backdrop);
    font-family:"Questrial",sans-serif;
    color:var(--ink);
    position:relative;
  }
  .sheet{position:absolute;background:var(--paper);box-shadow:0 2px 6px rgba(0,0,0,.18)}

  /* brand lockup */
  .brand{display:flex;align-items:center;gap:8px;color:var(--slate)}
  .brand__dot{border-radius:50%;background:var(--slate);flex:none}
  .brand__name{text-transform:uppercase;line-height:1.05;letter-spacing:.02em}
  .brand--light{color:var(--paper)}
  .brand--light .brand__dot{background:var(--paper)}

  .contact{text-align:right;line-height:1.35;color:var(--ink);white-space:nowrap}
  .contact__gap{height:.8em}

  /* business card front */
  .card-front{left:40px;top:50px;width:255px;height:150px;overflow:hidden}
  .card-front .brand{position:absolute;left:14px;top:36px}
  .card-front .brand__dot{width:18px;height:18px}
  .card-front .brand__name{font-size:12px;width:90px}
  .card-front .contact{position:absolute;left:142px;top:8px;font-size:6px;line-height:1.25;text-align:left}
  .card-front .contact__gap{height:.7em}
  .card-front .rule{position:absolute;left:12px;right:12px;top:114px;border-top:1px solid var(--rule)}
  .card-front .tagline{position:absolute;left:0;right:0;top:119px;text-align:center;font-size:7px;line-height:1.35}

  /* business card back */
  .card-back{left:315px;top:50px;width:255px;height:150px;background:var(--slate)}
  .card-back .brand{position:absolute;left:50%;top:50%;transform:translate(-50%,-50%)}
  .card-back .brand__dot{width:30px;height:30px}
  .card-back .brand__name{font-size:18px;width:140px}

  /* compliments slip */
  .comp{left:40px;top:240px;width:520px;height:245px;overflow:hidden}
  .comp__stripe{position:absolute;left:0;top:0;bottom:0;width:14px;background:var(--slate)}
  .comp .brand{position:absolute;left:30px;top:26px}
  .comp .brand__dot{width:24px;height:24px}
  .comp .brand__name{font-size:15px;width:130px}
  .comp .contact{position:absolute;right:22px;top:14px;font-size:8px;line-height:1.3}
  .comp__title{position:absolute;right:22px;top:148px;font-size:20px;color:var(--slate);letter-spacing:.02em}
  .comp__rule{position:absolute;left:30px;right:22px;top:176px;border-top:1px solid var(--rule)}
  .comp .tagline{position:absolute;right:22px;top:181px;font-size:8px;text-align:right;line-height:1.4}
  .comp__services{position:absolute;left:14px;right:0;bottom:0;height:22px;background:var(--slate);color:var(--paper);font-size:7.5px;padding:7px 16px;white-space:nowrap}

  /* letterhead */
  .letterhead{left:600px;top:50px;width:560px;height:792px}
  .letterhead__band{position:absolute;right:0;top:0;bottom:0;width:30px;background:var(--slate)}
  .letterhead .brand{position:absolute;left:30px;top:30px}
  .letterhead .brand__dot{width:34px;height:34px}
  .letterhead .brand__name{font-size:20px;width:170px}
  .letterhead .contact{position:absolute;right:48px;top:22px;font-size:9px}

  /* standalone logo for email signature */
  .signature-logo{left:40px;top:540px;width:520px;height:150px;display:flex;align-items:center;justify-content:center}
  .signature-logo .brand{gap:14px}
  .signature-logo .brand__dot{width:52px;height:52px}
  .signature-logo .brand__name{font-size:32px;width:270px}
</style>
</head>
<body>

  <section class="sheet card-front" aria-label="Business card front">
    <div class="brand"><span class="brand__dot"></span><span class="brand__name">Thomas Henley Limited</span></div>
    <div class="contact">
      <div>Tom Henley (FCMA)</div>
      <div class="contact__gap"></div>
      <div>Thomas Henley Limited</div>
      <div>Willow Brook Cottage</div>
      <div>Fenn</div>
      <div>Ashcombe</div>
      <div>Merrowshire</div>
      <div>TR8 2PW</div>
      <div class="contact__gap"></div>
      <div>t 07700-900412</div>
      <div>e tbhenley@tbhenley.co.uk</div>
      <div>w www.tbhenley.co.uk</div>
    </div>
    <div class="rule"></div>
    <div class="tagline">Providing Part time Finance Director Services<br>Full time results | Part time costs</div>
  </section>

  <section class="sheet card-back" aria-label="Business card back">
    <div class="brand brand--light"><span class="brand__dot"></span><span class="brand__name">Thomas Henley Limited</span></div>
  </section>

  <section class="sheet comp" aria-label="Compliments slip">
    <div class="comp__stripe"></div>
    <div class="brand"><span class="brand__dot"></span><span class="brand__name">Thomas Henley Limited</span></div>
    <div class="contact">
      <div>Tom Henley (FCMA)</div>
      <div class="contact__gap"></div>
      <div>Thomas Henley Limited</div>
      <div>Willow Brook Cottage</div>
      <div>Fenn</div>
      <div>Ashcombe</div>
      <div>Merrowshire</div>
      <div>TR8 2PW</div>
      <div class="contact__gap"></div>
      <div>07700-900412 | t</div>
      <div>tbhenley@tbhenley.co.uk | e</div>
      <div>www.tbhenley.co.uk | w</div>
    </div>
    <div class="comp__title">WITH COMPLIMENTS</div>
    <div class="comp__rule"></div>
    <div class="tagline">Providing Part time Finance Director Services<br>Full time results | Part time costs</div>
    <div class="comp__services">Management accounting | Interim management | Business plans | Budgeting &amp; forecasting | Payroll services | Project management</div>
  </section>

  <section class="sheet letterhead" aria-label="Letterhead">
    <div class="letterhead__band"></div>
    <div class="brand"><span class="brand__dot"></span><span class="brand__name">Thomas Henley Limited</span></div>
    <div class="contact">
      <div>Tom Henley (FCMA)</div>
      <div class="contact__gap"></div>
      <div>Thomas Henley Limited</div>
      <div>Willow Brook Cottage</div>
      <div>Fenn</div>
      <div>Ashcombe</div>
      <div>Merrowshire</div>
      <div>TR8 2PW</div>
      <div class="contact__gap"></div>
      <div>07700-900412 | t</div>
      <div>tbhenley@tbhenley.co.uk | e</div>
      <div>www.tbhenley.co.uk | w</div>
    </div>
  </section>

  <section class="sheet signature-logo" aria-label="Logo for email signature">
    <div class="brand"><span class="brand__dot"></span><span class="brand__name">Thomas Henley Limited</span></div>
  </section>

</body>
</html>
```